HIgh-end jewelry designer needs a business card design

I need a business card design for the ecclectic & rather expensive jewelry designs. My approach to my work is to combine very old jewelry offset with contemporary items. I enjoy the idea of legacy as well as repurposing finely crafted items that are not possible to create any longer. My desire is to celebrate the past in a contemporary & funky way. The name of my business is MERIVALE. I see my business card design as simple & yet enigmatic as possible. In the end... clean, simple & understated is the look I am after. Thank you for your consideration...

Target Market(s)

I will use this business card for the trade as well as customers

Industry/Entity Type

Business

Contact Information for Business Card

Corinne Halvard Owner/Designer 555-274-8163

Requirements
Must have
• Clean & simple sophisticated design using the word "Merivalle" as the logo. I like the idea of a play on the word itself, perhaps even using different fonts (i.e.: a bold helvetica combined with a lovely script). I'm afraid to say more because I don't want to limit creative input. Gosh, sometimes it's ok to break the rules!
Nice to have
• In my mind, I have imagined this business card to be simple, using my company name "Merivale" in a playful yet sophisticated manner. I believe that doing something beautifully simple can be a true challenge. I have imagined something with just black & white, however I am open to ideas... after all that's why I'm here!
Should not have
• As Mozart once said... "It has too many notes!" I know I'm being silly, but I don't want it to be complicated or overly ornate.

```html
<!DOCTYPE html>
<html lang="en">
<head>
<meta charset="UTF-8">
<title>Merivale — Business Card</title>
<link rel="stylesheet" href="https://fonts.googleapis.com/css2?family=Italianno&family=Questrial&display=swap">
<style>
  :root {
    --backdrop: #e9e7ea;
    --card-plum: #2f2238;
    --card-charcoal: #28252b;
    --ink-silver: #cfcfd3;
    --ink-soft: #b9b7bd;
    --bead: #e6e6e8;
  }
  * { margin: 0; padding: 0; box-sizing: border-box; }
  html, body {
    width: 1200px;
    height: 800px;
    overflow: hidden;
    background: var(--backdrop);
  }
  .card {
    position: absolute;
    left: 50px;
    top: 94px;
    width: 1100px;
    height: 612px;
    background: var(--card-plum);
    overflow: hidden;
  }
  .card-shade {
    position: absolute;
    inset: 0;
    width: 1100px;
    height: 612px;
  }
  .holder-name {
    position: absolute;
    left: 0;
    width: 100%;
    top: 196px;
    text-align: center;
    font-family: "Italianno", cursive;
    font-size: 46px;
    color: var(--ink-silver);
    letter-spacing: 2px;
  }
  .brand {
    position: absolute;
    left: 0;
    width: 100%;
    top: 280px;
    display: flex;
    justify-content: center;
    align-items: center;
    gap: 12px;
  }
  .brand-square {
    width: 16px;
    height: 16px;
    background: var(--ink-silver);
  }
  .brand-name {
    font-family: "Questrial", sans-serif;
    font-size: 26px;
    letter-spacing: 6px;
    color: var(--ink-silver);
  }
  .holder-role {
    position: absolute;
    left: 0;
    width: 100%;
    top: 384px;
    text-align: center;
    font-family: "Questrial", sans-serif;
    font-size: 21px;
    color: var(--ink-soft);
    letter-spacing: 0.5px;
  }
  .holder-phone {
    position: absolute;
    left: 0;
    width: 100%;
    top: 543px;
    text-align: center;
    font-family: "Questrial", sans-serif;
    font-size: 23px;
    color: var(--ink-soft);
    letter-spacing: 1px;
  }
  .bead-line {
    position: absolute;
    left: 0;
    top: 572px;
    width: 1100px;
    height: 8px;
  }
</style>
</head>
<body>
  <div class="card">
    <svg class="card-shade" viewBox="0 0 1100 612" aria-hidden="true">
      <polygon points="31,0 1100,0 1100,600" fill="var(--card-charcoal)"/>
    </svg>

    <div class="holder-name">Corinne Halvard</div>

    <div class="brand">
      <span class="brand-square"></span>
      <span class="brand-name">MERIVALE</span>
    </div>

    <div class="holder-role">Owner/Designer</div>

    <div class="holder-phone">555-274-8163</div>

    <svg class="bead-line" viewBox="0 0 1100 8" aria-hidden="true">
      <line x1="2" y1="4" x2="1098" y2="4" stroke="var(--bead)" stroke-width="3.5" stroke-linecap="round" stroke-dasharray="0.1 5"/>
    </svg>
  </div>
</body>
</html>
```